ZEPRILO.COM is a premium domain sales company. Our competitors are companies like vastplots.example, getparcels.example, peerwords.example. Our current site is at www.zeprilos.example.

We want to have the ability to search for domains, to highlight special offers and have some testimonials on the index page.

The logo for the site is attached.

Please be sure that the order form fits on the screen without scrolling the page. I want the entire form, including the submit button to fit without any page scrolling.

Delivered product - INDEX PAGE, ORDER FORM AND CONTENT PAGE PSDs.

Target Market(s)

Small to Medium business professionals

Industry/Entity Type

It Company

Requirements
Must have
• 1. List of domains for sale
2. Simple search box with button to run the search
3. link for advanced search
4. testimonial area. Note - this can be a small box where a different testimonial is displayed on each page load.
Nice to have
• Would like the site to have some white space. Don't want a heavily packed website. Give it an "airy" feel.

```html
<!DOCTYPE html>
<html lang="en">
<head>
<meta charset="utf-8">
<title>ZEPRILO.COM – Your order</title>
<link href="https://fonts.googleapis.com/css2?family=Zilla+Slab:ital,wght@0,300;0,400;1,300;1,400&family=Lato:wght@400&display=swap" rel="stylesheet">
<style>
:root{
  --blue:#0b4f9c;
  --blue-dark:#0a4a93;
  --red:#d9262b;
  --ink:#3d3d3d;
  --line:#dcdcdc;
  --header-bg:#f7f7f7;
  --white:#ffffff;
}
*{box-sizing:border-box;margin:0;padding:0}
html,body{width:1007px;height:1200px;overflow:hidden;background:var(--white)}
body{font-family:"Zilla Slab",Georgia,serif;color:var(--ink);position:relative}
.page{position:relative;width:1007px;height:1200px;overflow:hidden}

/* header */
.site-header{position:absolute;left:0;top:0;width:1007px;height:63px;background:var(--header-bg);border-bottom:2px solid #d6d6d6}
.brand{position:absolute;left:75px;top:18px;display:flex;align-items:center;gap:7px;font-weight:400;font-size:25px;color:var(--blue);letter-spacing:.5px}
.brand-dot{width:14px;height:14px;border-radius:50%;background:var(--blue)}
.main-nav{position:absolute;left:317px;top:0;height:63px;display:flex}
.main-nav a{display:flex;align-items:center;justify-content:center;height:63px;border-left:1px solid var(--line);font-size:21px;color:var(--ink);text-decoration:none}
.main-nav .cart{border-right:1px solid var(--line);position:relative;border-bottom:5px solid var(--blue);height:63px;background:var(--white)}
.cart-badge{position:absolute;left:35px;top:11px;width:17px;height:17px;border-radius:50%;background:var(--red);color:var(--white);font-family:Lato,sans-serif;font-size:10px;display:flex;align-items:center;justify-content:center}

/* order form */
.order-title{position:absolute;left:72px;top:104px;font-size:51px;font-weight:300;color:var(--blue);line-height:1}
.order-title em{font-style:italic}
.intro{position:absolute;left:73px;top:180px;width:460px;font-family:Lato,sans-serif;font-size:10.8px;line-height:16px;color:var(--ink)}
.field{position:absolute;height:50px;border:1px solid var(--blue);padding-left:17px;display:flex;align-items:center;font-size:20.5px;font-weight:300;color:var(--ink)}
.field.full{left:73px;width:431px}
.btn-order{position:absolute;left:73px;top:581px;width:135px;height:48px;background:var(--blue-dark);color:var(--white);font-size:21px;font-weight:300;display:flex;align-items:center;justify-content:center}
.next-step{position:absolute;left:224px;top:596px;font-size:15.5px;font-style:italic;font-weight:300;color:var(--blue)}

/* basket table */
.basket{position:absolute;left:597px;top:158px;width:335px;border-collapse:collapse;background:var(--white);box-shadow:0 0 4px rgba(0,0,0,.15);font-size:17px;font-weight:300}
.basket td,.basket th{height:47px;border-bottom:1px solid var(--line);font-weight:300}
.basket th{color:var(--blue);text-align:left;font-weight:400}
.basket .col-name{padding-left:10px;width:225px;border-right:1px solid var(--line)}
.basket .col-cost{width:64px;text-align:center;color:var(--red);border-right:1px solid var(--line)}
.basket th.col-cost{color:var(--blue);text-align:center}
.basket .col-del{text-align:center}
.del{display:inline-flex;width:29px;height:29px;background:var(--red);border-radius:2px;align-items:center;justify-content:center}
.basket tr.total td{height:48px;border-bottom:none;border-right:none;border-top:2px solid var(--line)}
.basket tr.total .col-name{color:var(--blue)}
.basket tr.total .col-cost{font-weight:400}

.pay-note{position:absolute;left:607px;top:459px;font-size:17px;line-height:19px;font-weight:300;color:var(--blue)}
.pay-method{position:absolute;font-size:20px;font-weight:400;color:var(--blue)}

/* testimonial band */
.testimonial-band{position:absolute;left:0;top:693px;width:1007px;height:462px;background:linear-gradient(90deg,#5a4535 0%,#8a7563 20%,#b9a79a 38%,#ddd1cb 55%,#e6dcd8 75%,#9a7d6a 90%,#c9b8ae 100%);border-top:1px solid var(--line)}
.testimonial-card{position:absolute;left:421px;top:748px;width:512px;height:369px;background:var(--white);box-shadow:0 0 4px rgba(0,0,0,.12);padding:20px 28px}
.testimonial-card h2{font-size:49px;font-weight:300;color:var(--blue);line-height:46px;margin-bottom:30px}
.testimonial-card h2 em{font-style:italic}
.testimonial-card p{font-family:Lato,sans-serif;font-size:10.8px;line-height:16px;color:var(--ink);margin-bottom:8px}
.author{font-size:26px;font-weight:400;color:var(--blue);margin-top:12px}
.company{font-size:16px;font-weight:300;color:var(--blue);line-height:17px;margin-top:5px}
.company em{font-style:italic;display:block}

/* footer */
.site-footer{position:absolute;left:0;top:1155px;width:1007px;height:45px;border-top:1px solid var(--line);background:var(--white);font-size:12.5px;font-weight:300;color:var(--ink)}
.copyright{position:absolute;left:75px;top:15px}
.footer-links{position:absolute;right:75px;top:15px}
</style>
</head>
<body>
<div class="page">

  <header class="site-header">
    <div class="brand"><span class="brand-dot"></span>ZEPRILO.COM</div>
    <nav class="main-nav">
      <a href="#" style="width:124px">Domains</a>
      <a href="#" style="width:98px">FAQs</a>
      <a href="#" style="width:126px">About us</a>
      <a href="#" style="width:114px">Contact</a>
      <a href="#" style="width:94px">Login</a>
      <a href="#" class="cart" style="width:59px" aria-label="Basket">
        <svg width="24" height="22" viewBox="0 0 24 22" aria-hidden="true">
          <path d="M1 2h4l3 11h11l3-8H7" fill="none" stroke="#0b4f9c" stroke-width="2.4" stroke-linejoin="round"/>
          <rect x="8" y="6" width="12" height="6" fill="#0b4f9c"/>
          <circle cx="9.5" cy="18" r="2" fill="#0b4f9c"/>
          <circle cx="18" cy="18" r="2" fill="#0b4f9c"/>
        </svg>
        <span class="cart-badge">4</span>
      </a>
    </nav>
  </header>

  <h1 class="order-title">1. Your <em>order.</em></h1>
  <p class="intro">Lorem ipsum dolor sit amet, consectetur adipiscing elit. Praesent nec erat ut nunc ultrices suscipit in in dui. Fusce adipiscing nisi eget ligula placerat hendrerit. Cras posuere sagittis tellus nec porta.</p>

  <div class="field full" style="top:248px">Name</div>
  <div class="field full" style="top:315px">Email address</div>
  <div class="field full" style="top:381px">Address line 1</div>
  <div class="field full" style="top:447px">Address line 2</div>
  <div class="field" style="top:513px;left:73px;width:208px">State/Province</div>
  <div class="field" style="top:513px;left:296px;width:208px">Zip code</div>

  <div class="btn-order">Place order</div>
  <div class="next-step">Next Step: Payment details.</div>

  <table class="basket">
    <tr><th class="col-name">Domains bought</th><th class="col-cost">Cost</th><th class="col-del"></th></tr>
    <tr><td class="col-name">tim-harlow.com</td><td class="col-cost">$97</td><td class="col-del"><span class="del"><svg width="11" height="11" viewBox="0 0 11 11"><path d="M1.5 1.5l8 8M9.5 1.5l-8 8" stroke="#fff" stroke-width="2.6"/></svg></span></td></tr>
    <tr><td class="col-name">instant-office.com</td><td class="col-cost">$100</td><td class="col-del"><span class="del"><svg width="11" height="11" viewBox="0 0 11 11"><path d="M1.5 1.5l8 8M9.5 1.5l-8 8" stroke="#fff" stroke-width="2.6"/></svg></span></td></tr>
    <tr><td class="col-name">slicedealvouchers.com</td><td class="col-cost">$397</td><td class="col-del"><span class="del"><svg width="11" height="11" viewBox="0 0 11 11"><path d="M1.5 1.5l8 8M9.5 1.5l-8 8" stroke="#fff" stroke-width="2.6"/></svg></span></td></tr>
    <tr><td class="col-name">carrywallets.com</td><td class="col-cost">$5,000</td><td class="col-del"><span class="del"><svg width="11" height="11" viewBox="0 0 11 11"><path d="M1.5 1.5l8 8M9.5 1.5l-8 8" stroke="#fff" stroke-width="2.6"/></svg></span></td></tr>
    <tr class="total"><td class="col-name">Grand total</td><td class="col-cost">$5,594</td><td></td></tr>
  </table>

  <p class="pay-note">We accept the following<br>methods of payment:</p>
  <span class="pay-method" style="left:612px;top:523px">Cardora</span>
  <span class="pay-method" style="left:727px;top:523px">Vestra</span>
  <span class="pay-method" style="left:862px;top:523px">Amplex</span>
  <span class="pay-method" style="left:643px;top:583px">PayLoop</span>
  <span class="pay-method" style="left:790px;top:583px">Findera</span>

  <div class="testimonial-band" role="img" aria-label="Photo of a smiling craftsman in a denim shirt and apron leaning in his joinery workshop, tools hanging on the wall behind him"></div>

  <section class="testimonial-card">
    <h2>Our success is all<br>down to <em>your success.</em></h2>
    <p>Lorem ipsum dolor sit amet, consectetur adipiscing elit. Praesent nec erat ut nunc ultrices suscipit in in dui. Fusce adipiscing nisi eget ligula placerat hendrerit. Cras posuere sagittis tellus nec porta.</p>
    <p>Fusce libero magna, lacinia in blandit eu, posuere in augue. Phasellus interdum velit non eros commodo a viverra lectus tempor. Nunc vel magna quam, vitae dignissim mi. Mauris pellentesque sapien et nisl interdum elementum nec vitae mi. Lorem ipsum dolor sit amet, consectetur adipiscing elit.</p>
    <div class="author">Walter Penhale Snr.</div>
    <div class="company">Penhale &amp; son Joinery<em>www.penhalejoinery.example</em></div>
  </section>

  <footer class="site-footer">
    <span class="copyright">© copyright 2013 ZEPRILO.COM Ltd. All rights reserved.</span>
    <span class="footer-links">Login &nbsp;•&nbsp; Register &nbsp;•&nbsp; ZEPRILO support &nbsp;•&nbsp; Terms &amp; conditions &nbsp;•&nbsp; Privacy policy</span>
  </footer>

</div>
</body>
</html>
```